Landscaping flier 2024

Create a 1 page flier for landscaping services
1. Must be completed in Adobe Photoshop
2. Size 8.5" x 11" (portrait layout)
3. Include logo
4. Text to include:
2024 Gravesite Landscaping Packages
info@maplecrestmemorial.example
(201) 555-0148
maplecrestmemorial.example
5. Use chart text for the content. DO NOT COPY THE CHART DESIGN/FORMAT. Use the chart for the text you need only.
6. Use "Pricing cards as format for laying out the chart". Open to other ideas as well.
**Use the example of chart design (handwritten) to base your design off of.
7. Photos
-include before and after care photos

```html
<!DOCTYPE html>
<html lang="en">
<head>
<meta charset="utf-8">
<title>2024 Gravesite Landscaping Packages</title>
<link href="https://fonts.googleapis.com/css2?family=Poppins:wght@300;400;500;600;700;800&display=swap" rel="stylesheet">
<style>
:root{
  --forest:#1f5f25;
  --forest-deep:#154a1a;
  --forest-card:rgba(18,70,22,.55);
  --gold:#e2aa12;
  --gold-deep:#c99200;
  --paper:#ebebeb;
  --backdrop:#a4a4a4;
  --ink:#2c2c2c;
  --white:#ffffff;
  --brand:#7a1f1f;
}
*{box-sizing:border-box;margin:0;padding:0}
html,body{width:1200px;height:900px;overflow:hidden}
body{background:var(--backdrop);font-family:'Poppins',sans-serif;position:relative}
.flier{position:absolute;left:270px;top:23px;width:660px;height:854px;background:var(--paper);overflow:hidden;box-shadow:0 8px 24px rgba(0,0,0,.25)}
.hero{position:absolute;left:0;top:0;width:660px;height:600px;background:radial-gradient(ellipse at 70% 20%,#3b7a33 0%,#24632a 40%,#174f1c 100%)}
.hero-photo{position:absolute;left:0;top:0;width:100%;height:100%;background:linear-gradient(180deg,rgba(60,110,50,.35),rgba(20,70,25,.1) 50%,rgba(70,110,60,.35))}
.corner{position:absolute;background:var(--gold)}
.corner.tl{left:0;top:0;width:50px;height:36px;border-bottom-right-radius:10px}
.corner.tr{right:0;top:0;width:38px;height:36px;border-bottom-left-radius:10px}
.corner-line{position:absolute;border:1px solid var(--gold);}
.corner-line.tl{left:-1px;top:-1px;width:66px;height:68px;border-top:none;border-left:none;border-bottom-right-radius:12px}
.corner-line.tr{right:-1px;top:-1px;width:56px;height:68px;border-top:none;border-right:none;border-bottom-left-radius:12px}
.diamond-outline{position:absolute;width:36px;height:36px;border:1px solid var(--gold);transform:rotate(45deg)}
.badge{position:absolute;left:186px;top:28px;width:290px;height:100px}
.badge-title{position:absolute;left:0;top:10px;width:290px;text-align:center;color:var(--white);font-weight:700;font-size:48px;line-height:1}
.badge-sub{position:absolute;left:0;top:60px;width:290px;text-align:center;color:var(--forest-deep);font-weight:700;font-size:24px;line-height:1.2}
.subtitle{position:absolute;left:220px;top:144px;color:var(--white);font-weight:400;font-size:19px}
.popular-pill{position:absolute;left:514px;top:148px;width:96px;height:22px;border-radius:11px;background:var(--forest);color:var(--gold);font-size:10px;font-weight:600;text-align:center;line-height:22px}
.services-title{position:absolute;left:27px;top:197px;color:var(--white);font-weight:600;font-size:26px;line-height:1.25}
.service{position:absolute;left:27px;color:var(--white);font-weight:500;font-size:12.5px;line-height:1.2;width:170px}
.card{position:absolute;top:185px;width:134px;height:481px;border:1px solid var(--gold);border-radius:10px;overflow:hidden;background:var(--forest-card);color:var(--white);text-align:center}
.card.featured{background:var(--gold);border-color:var(--gold);color:var(--forest)}
.card-name{margin-top:14px;font-size:13px;font-weight:500;line-height:1.25}
.card-desc{margin:4px 4px 0;font-size:8.5px;font-weight:600;line-height:1.25}
.card-schedule{position:absolute;left:14px;right:14px;top:90px;font-size:6.5px;line-height:1.3;opacity:.9}
.mark{position:absolute;left:0;width:100%;font-size:13px;font-weight:500}
.no-icon{position:absolute;left:55px;width:24px;height:24px}
.card-foot{position:absolute;left:0;bottom:0;width:100%;height:93px;background:var(--forest);border-top:1px solid var(--gold)}
.card.featured .card-foot{background:var(--gold);border-top-color:var(--gold-deep)}
.term-pills{display:flex;justify-content:space-between;padding:8px 8px 0}
.term-pill{background:var(--gold);color:var(--white);font-size:7px;border-radius:6px;padding:1px 5px}
.term-prices{display:flex;justify-content:space-between;padding:8px 9px 0;font-size:14px}
.foot-label{margin-top:10px;font-size:8px;font-weight:300}
.foot-price{font-size:28px;font-weight:400;line-height:1.2}
.foot-note{margin-top:4px;font-size:8px;font-weight:300;line-height:1.25}
.card.featured .foot-label,.card.featured .foot-note{color:var(--forest)}
.gold-corner{position:absolute;left:-40px;top:620px;width:100px;height:130px;background:var(--gold);clip-path:polygon(0 0,50% 0,100% 50%,50% 100%,0 100%)}
.valid{position:absolute;left:76px;top:642px;font-size:8.5px;color:var(--ink)}
.brand{position:absolute;left:22px;top:732px;width:115px;display:flex;flex-direction:column;align-items:center;gap:6px}
.brand-dot{width:26px;height:26px;border-radius:50%;background:var(--brand)}
.brand-name{color:var(--brand);font-size:17px;font-weight:500;line-height:1.1;text-align:center}
.divider{position:absolute;left:148px;top:708px;width:1px;height:104px;background:#bbb}
.contact{position:absolute;left:162px;display:flex;align-items:center;gap:9px;font-size:11.5px;color:var(--forest);white-space:nowrap}
.contact svg{width:14px;height:14px;flex:none}
.photo{position:absolute;top:722px;width:76px;height:76px;transform:rotate(45deg);border:4px solid var(--gold);border-radius:8px;overflow:hidden}
.photo-fill{width:100%;height:100%;background:linear-gradient(135deg,#5f8a3a,#2f5e1f 60%,#8aa46a)}
.photo-label{position:absolute;top:815px;width:104px;text-align:center;font-size:11px;font-weight:600;color:var(--forest)}
</style>
</head>
<body>
<main class="flier">
  <section class="hero">
    <div class="hero-photo" role="img" aria-label="Photo of a tree-lined cemetery with headstones, tinted green"></div>
    <div class="corner tl"></div><div class="corner tr"></div>
    <div class="corner-line tl"></div><div class="corner-line tr"></div>
    <div class="diamond-outline" style="left:80px;top:102px"></div>
    <div class="diamond-outline" style="left:148px;top:349px"></div>

    <div class="badge">
      <svg width="290" height="100" viewBox="0 0 290 100">
        <path d="M40 2 H250 L282 50 L250 98 H40 L8 50 Z" fill="none" stroke="#e2aa12" stroke-width="2" stroke-linejoin="round"/>
        <path d="M48 8 H242 L270 50 L242 92 H48 L20 50 Z" fill="#e2aa12" stroke-linejoin="round"/>
      </svg>
      <div class="badge-title">2024</div>
      <div class="badge-sub">Gravesite</div>
    </div>
    <div class="subtitle">Landscaping Packages</div>
    <div class="popular-pill">MOST POPULAR</div>

    <h2 class="services-title">SERVICES<br>OFFERED</h2>
    <div class="service" style="top:278px">WEEDING &amp; TRIMMING<br>ON YOUR GRAVESITE</div>
    <div class="service" style="top:321px">PAYMENT ENSURES<br>GRAVE CARE FOREVER</div>
    <div class="service" style="top:373px">MONUMENT CLEANING</div>
    <div class="service" style="top:416px">MONUMENT LEVELING</div>
    <div class="service" style="top:450px">FULL BED OF BOXWOOD<br>SHRUBS</div>
    <div class="service" style="top:492px">REPLACEMENT<br>OF SHRUBS</div>
    <div class="service" style="top:544px">TRUST CERTIFICATE</div>
  </section>

  <article class="card" style="left:212px">
    <div class="card-name">SEASONAL<br>CARE</div>
    <div class="card-desc">Seasonal landscaping<br>grave care</div>
    <div class="card-schedule">Approximately every 7 weeks during the growing season: mid-April through mid-October</div>
    <svg class="no-icon" style="top:132px" viewBox="0 0 24 24"><circle cx="12" cy="12" r="10" fill="none" stroke="#fff" stroke-width="1.6"/><line x1="5" y1="19" x2="19" y2="5" stroke="#fff" stroke-width="1.6"/></svg>
    <svg class="no-icon" style="top:175px" viewBox="0 0 24 24"><circle cx="12" cy="12" r="10" fill="none" stroke="#fff" stroke-width="1.6"/><line x1="5" y1="19" x2="19" y2="5" stroke="#fff" stroke-width="1.6"/></svg>
    <svg class="no-icon" style="top:218px" viewBox="0 0 24 24"><circle cx="12" cy="12" r="10" fill="none" stroke="#fff" stroke-width="1.6"/><line x1="5" y1="19" x2="19" y2="5" stroke="#fff" stroke-width="1.6"/></svg>
    <svg class="no-icon" style="top:260px" viewBox="0 0 24 24"><circle cx="12" cy="12" r="10" fill="none" stroke="#fff" stroke-width="1.6"/><line x1="5" y1="19" x2="19" y2="5" stroke="#fff" stroke-width="1.6"/></svg>
    <svg class="no-icon" style="top:303px" viewBox="0 0 24 24"><circle cx="12" cy="12" r="10" fill="none" stroke="#fff" stroke-width="1.6"/><line x1="5" y1="19" x2="19" y2="5" stroke="#fff" stroke-width="1.6"/></svg>
    <svg class="no-icon" style="top:344px" viewBox="0 0 24 24"><circle cx="12" cy="12" r="10" fill="none" stroke="#fff" stroke-width="1.6"/><line x1="5" y1="19" x2="19" y2="5" stroke="#fff" stroke-width="1.6"/></svg>
    <div class="card-foot">
      <div class="term-pills"><span class="term-pill">3 Years</span><span class="term-pill">2 Years</span><span class="term-pill">1 Year</span></div>
      <div class="term-prices"><span>$396</span><span>$264</span><span>$132</span></div>
      <div class="foot-note" style="margin-top:12px">Multi-year payment<br>locks in current rates</div>
    </div>
  </article>

  <article class="card" style="left:354px">
    <div class="card-name">BASIC CARE<br>ENDOWMENT</div>
    <div class="card-desc">Landscaping care forever<br>for graves with no planting.</div>
    <div class="card-schedule" style="top:92px">2 times per year:<br>mid-May &amp;<br>mid-September</div>
    <div class="mark" style="top:136px">YES</div>
    <div class="mark" style="top:179px">YES</div>
    <svg class="no-icon" style="top:218px" viewBox="0 0 24 24"><circle cx="12" cy="12" r="10" fill="none" stroke="#fff" stroke-width="1.6"/><line x1="5" y1="19" x2="19" y2="5" stroke="#fff" stroke-width="1.6"/></svg>
    <svg class="no-icon" style="top:260px" viewBox="0 0 24 24"><circle cx="12" cy="12" r="10" fill="none" stroke="#fff" stroke-width="1.6"/><line x1="5" y1="19" x2="19" y2="5" stroke="#fff" stroke-width="1.6"/></svg>
    <svg class="no-icon" style="top:303px" viewBox="0 0 24 24"><circle cx="12" cy="12" r="10" fill="none" stroke="#fff" stroke-width="1.6"/><line x1="5" y1="19" x2="19" y2="5" stroke="#fff" stroke-width="1.6"/></svg>
    <svg class="no-icon" style="top:344px" viewBox="0 0 24 24"><circle cx="12" cy="12" r="10" fill="none" stroke="#fff" stroke-width="1.6"/><line x1="5" y1="19" x2="19" y2="5" stroke="#fff" stroke-width="1.6"/></svg>
    <div class="card-foot">
      <div class="foot-label">12 monthly payment of</div>
      <div class="foot-price">$287</div>
      <div class="foot-note">Call for single<br>payment discount</div>
    </div>
  </article>

  <article class="card featured" style="left:496px">
    <div class="card-name">PERPETUAL CARE<br>ENDOWMENT</div>
    <div class="card-desc">Landscaping care forever<br>for graves with planting.</div>
    <div class="card-schedule">Approximately every 7 weeks during the growing season: mid-April through mid-October</div>
    <div class="mark" style="top:136px">YES</div>
    <div class="mark" style="top:179px">YES</div>
    <div class="mark" style="top:222px">YES</div>
    <div class="mark" style="top:264px">YES</div>
    <div class="mark" style="top:307px">YES</div>
    <div class="mark" style="top:348px">YES</div>
    <div class="card-foot">
      <div class="foot-label">12 monthly payment of</div>
      <div class="foot-price">$351</div>
      <div class="foot-note">Call for single<br>payment discount</div>
    </div>
  </article>

  <div class="gold-corner"></div>
  <div class="valid">Valid through 10/31/2024</div>

  <div class="brand">
    <span class="brand-dot"></span>
    <span class="brand-name">Maplecrest<br>Memorial</span>
  </div>
  <div class="divider"></div>

  <div class="contact" style="top:738px">
    <svg viewBox="0 0 24 24"><circle cx="12" cy="12" r="10" fill="none" stroke="#e2aa12" stroke-width="2"/><ellipse cx="12" cy="12" rx="4" ry="10" fill="none" stroke="#e2aa12" stroke-width="2"/><line x1="2" y1="12" x2="22" y2="12" stroke="#e2aa12" stroke-width="2"/></svg>
    maplecrestmemorial.example
  </div>
  <div class="contact" style="top:763px">
    <svg viewBox="0 0 24 24"><path d="M6 2 L10 6 L8 9 C9 12 12 15 15 16 L18 14 L22 18 L19 22 C10 21 3 14 2 5 Z" fill="#e2aa12"/></svg>
    (201) 555-0148
  </div>
  <div class="contact" style="top:788px">
    <svg viewBox="0 0 24 24"><rect x="2" y="5" width="20" height="14" fill="#e2aa12"/><path d="M2 5 L12 13 L22 5" fill="none" stroke="#fff" stroke-width="1.6"/></svg>
    info@maplecrestmemorial.example
  </div>

  <div class="photo" style="left:430px"><div class="photo-fill" role="img" aria-label="Before photo: untended gravesite with overgrown shrubs"></div></div>
  <div class="photo" style="left:552px"><div class="photo-fill" role="img" aria-label="After photo: neatly trimmed shrub bed around a headstone"></div></div>
  <div class="photo-label" style="left:416px">Before</div>
  <div class="photo-label" style="left:538px">After</div>
</main>
</body>
</html>
```